Gazebrix fresh re-design

We are UK based company and have Magento website which we are happy with, but we require fresh design. Menu must be customer friendly

Design must reflect in strength as strength of our products and value for money are our selling points.

Our products are not family products there mainly used for business at events, cycling, running clubs, etc

New design must have same information as current design

links that require new design

http://www.gazebrix.example (landing page)

http://www.gazebrix.example/3m-x-3m-heavy-duty-tents/3m-x-3m-pop-up-marquee-white.html (product page)

http://www.gazebrix.example/custom-design-own-tent-size/choose-3mx3m.html (design tool)

Target Market(s)

business owners, cycling clubs, running clubs,

Industry/Entity Type

It Company

Number of Pages Required

3 page

Requirements
Must have
• background image of working gazebrix, clean fresh design, printed gazebrixes eg. cupcake
Should not have
• all same functions as current page

```html
<!DOCTYPE html>
<html lang="en">
<head>
<meta charset="utf-8">
<title>Gazebrix – Home</title>
<link href="https://fonts.googleapis.com/css2?family=Source+Sans+3:wght@300;400;600;700&family=Bungee&display=swap" rel="stylesheet">
<style>
:root{
  --bar:#c8c8c8;
  --footer:#aaaaaa;
  --ink:#1c1c1c;
  --muted:#555555;
  --icon:#c6c6c6;
  --brand:#2a2f8f;
  --accent:#d8202c;
  --pink:#f27e7e;
  --purple:#7b78b5;
  --glow:rgba(150,175,140,.5);
  --btn:#c8c8c8;
  --sky:#a9d5e6;
  --canopy:#1f9d7a;
  --canopy-dark:#12785c;
  --trees:#3e4a3a;
  --grass:#b9b88f;
  --lawn:#5e983c;
  --print-red:#c22a3c;
}
*{margin:0;padding:0;box-sizing:border-box}
html,body{width:1200px;height:3089px;overflow:hidden;background:#fff}
body{position:relative;font-family:"Source Sans 3",Arial,sans-serif;color:var(--ink)}
.abs{position:absolute}

/* header */
.topbar{left:0;top:0;width:1200px;height:49px;background:var(--bar);font-size:15px}
.topbar span{position:absolute;top:16px;line-height:1}
.brand{left:55px;top:112px;display:flex;align-items:center;gap:14px}
.brand-mark{width:26px;height:26px;background:var(--accent)}
.brand-name{font-size:44px;font-weight:600;color:var(--brand);line-height:1}
.nav a{position:absolute;top:141px;font-size:27px;color:var(--ink);text-decoration:none;line-height:1}

/* hero */
.hero{left:2px;top:243px;width:599px;height:407px;
  background:
    radial-gradient(ellipse 150px 90px at 150px 330px,rgba(194,42,60,.95),rgba(194,42,60,0) 100%),
    radial-gradient(ellipse 130px 80px at 440px 335px,rgba(194,42,60,.9),rgba(194,42,60,0) 100%),
    linear-gradient(180deg,var(--sky) 0%,#dfeef3 40%,#eef3f2 62%,#9fbf7a 85%,#4f9a35 100%)}
.hero-title{left:83px;top:306px;font-family:"Bungee",sans-serif;font-size:35px;line-height:1;color:#111}
.hero-title .red{color:#d3214a}
.try-btn{left:365px;top:509px;width:190px;height:58px;background:var(--btn);font-size:21px;font-weight:300;display:flex;align-items:center;justify-content:center;color:#333;box-shadow:0 1px 3px rgba(0,0,0,.3)}

/* perks */
.perks{left:668px;top:244px;width:528px;height:418px;background:linear-gradient(135deg,var(--pink) 0%,var(--pink) 30%,#fff 36%,#fff 57%,var(--purple) 66%,var(--purple) 100%)}
.perk{position:absolute;left:107px;display:flex;align-items:center;gap:12px;font-size:21px;font-weight:300;color:#333}
.perk svg{width:70px;height:70px;flex:none}
.perk b{font-weight:700;color:#111}

/* categories */
.cat-icon{position:absolute;display:block}
.cat-label{position:absolute;width:240px;text-align:center;font-size:21px;font-weight:300;color:var(--muted);line-height:1}

/* products */
.section-title{left:0;width:1240px;text-align:center;font-size:32px;font-weight:400;line-height:1}
.gazebo-photo{background:
    linear-gradient(90deg,rgba(31,157,122,0) 18%,rgba(31,157,122,.9) 30%,rgba(18,120,92,.95) 50%,rgba(31,157,122,.9) 70%,rgba(31,157,122,0) 82%) 0 12%/100% 62% no-repeat,
    linear-gradient(180deg,#566452 0%,var(--trees) 30%,#7d8a66 45%,var(--grass) 70%,#cfcca8 100%)}
.product-img{position:absolute;top:1385px;height:185px}
.product-name,.product-price{position:absolute;font-size:26px;line-height:1;white-space:nowrap}
.chev{position:absolute;top:1455px;width:30px;height:40px}

/* features */
.feature-img{position:absolute;box-shadow:0 0 40px 14px var(--glow)}
.photo-bag{background:
    linear-gradient(160deg,rgba(0,0,0,0) 38%,#1a1a1a 44%,#222 58%,rgba(0,0,0,0) 64%),
    linear-gradient(180deg,#7f8c66 0%,#c9cec2 30%,#ececec 100%)}
.photo-frame{background:
    radial-gradient(ellipse 60px 50px at 50% 52%,#1e1e1e,rgba(30,30,30,0) 100%),
    linear-gradient(90deg,rgba(0,0,0,0) 40%,#9a9a9a 46%,#d8d8d8 50%,#9a9a9a 54%,rgba(0,0,0,0) 60%),
    linear-gradient(180deg,#eeeeee 0%,#c4c4c4 40%,#8e8e8e 60%,#dcdcdc 100%)}
.photo-print{background:
    radial-gradient(ellipse 130px 70px at 50% 55%,rgba(194,42,60,1),rgba(194,42,60,.6) 100%),
    linear-gradient(180deg,#e8eef0 0%,#e8eef0 15%,var(--print-red) 30%,#b2283a 75%,#6aa43d 100%)}
.photo-folded{background:
    radial-gradient(ellipse 45px 55px at 50% 38%,#d3124a,rgba(211,18,74,0) 100%),
    linear-gradient(90deg,rgba(0,0,0,0) 42%,#b8bcc0 46%,#d6d9dc 50%,#b8bcc0 54%,rgba(0,0,0,0) 58%) 0 60%/100% 45% no-repeat,
    linear-gradient(180deg,#7b8b74 0%,#6b5050 22%,#5d9138 40%,var(--lawn) 100%)}
.feature-label{position:absolute;font-size:33px;line-height:1;white-space:nowrap}

/* footer */
.footer{left:0;top:2818px;width:1200px;height:271px;background:var(--footer)}
.footer-note{position:absolute;left:0;top:139px;width:1050px;text-align:center;font-size:27px;line-height:1}
</style>
</head>
<body>

<header>
  <div class="abs topbar">
    <span style="left:53px">Call 1(555) 010 - 0199&nbsp;&nbsp;&nbsp;&nbsp;Email: info@gazebrix.example</span>
    <span style="left:1000px">My Account</span>
    <span style="left:1133px">Cart</span>
  </div>
  <div class="abs brand"><span class="brand-mark"></span><span class="brand-name">gazebrix</span></div>
  <nav class="nav">
    <a style="left:700px">Tents</a>
    <a style="left:796px">Parts</a>
    <a style="left:878px">Weights</a>
    <a style="left:1016px">Tables</a>
  </nav>
</header>

<section>
  <div class="abs hero" role="img" aria-label="Printed branded gazebos standing on grass under a blue sky"></div>
  <div class="abs hero-title">DESIGN YOUR<br><span class="red">OWN</span> TENT</div>
  <div class="abs try-btn">TRY IT NOW</div>

  <div class="abs perks">
    <div class="perk" style="top:56px">
      <svg viewBox="0 0 70 70"><path d="M66 4 L6 40 L26 44 Z" fill="#444"/><path d="M66 4 L26 44 L30 64 Z" fill="#222"/></svg>
      <span><b>FREE</b> SHIPPING</span>
    </div>
    <div class="perk" style="top:180px">
      <svg viewBox="0 0 70 70"><circle cx="35" cy="33" r="27" fill="#444"/><path d="M50 55 L62 64 L58 48 Z" fill="#444"/><circle cx="24" cy="33" r="3.5" fill="#fff"/><circle cx="35" cy="33" r="3.5" fill="#fff"/><circle cx="46" cy="33" r="3.5" fill="#fff"/></svg>
      <span>EXPERT <b>ADVICE</b></span>
    </div>
    <div class="perk" style="top:306px">
      <svg viewBox="0 0 70 70"><g fill="none" stroke="#444" stroke-width="8" stroke-linecap="round"><rect x="34" y="6" width="28" height="16" rx="8" transform="rotate(-45 48 14)"/><rect x="8" y="48" width="28" height="16" rx="8" transform="rotate(-45 22 56)"/><line x1="28" y1="42" x2="42" y2="28"/></g></svg>
      <span><b><i>SECURE</i></b> SHOPPING</span>
    </div>
  </div>
</section>

<section class="categories">
  <svg class="cat-icon" style="left:145px;top:752px" width="90" height="94" viewBox="0 0 90 94"><rect x="10" y="8" width="16" height="86" fill="var(--icon)"/><path d="M10 22 L40 18 L82 30 L82 40 L40 34 L26 40 Z" fill="var(--icon)"/><rect x="2" y="18" width="30" height="24" fill="#dcdcdc"/></svg>
  <span class="cat-label" style="left:70px;top:883px">PARTS</span>

  <svg class="cat-icon" style="left:452px;top:746px" width="100" height="94" viewBox="0 0 100 94"><path d="M50 2 L96 32 L4 32 Z" fill="var(--icon)"/><path d="M4 32 Q10 44 16 32 Q22 44 28 32 Q34 44 40 32 Q46 44 52 32 Q58 44 64 32 Q70 44 76 32 Q82 44 88 32 Q92 40 96 32" fill="var(--icon)"/><rect x="4" y="32" width="4" height="56" fill="var(--icon)"/><rect x="92" y="32" width="4" height="56" fill="var(--icon)"/><rect x="30" y="36" width="3" height="44" fill="var(--icon)"/><rect x="67" y="36" width="3" height="44" fill="var(--icon)"/></svg>
  <span class="cat-label" style="left:372px;top:883px">ROOFS</span>

  <svg class="cat-icon" style="left:711px;top:760px" width="120" height="94" viewBox="0 0 120 94"><rect x="2" y="10" width="116" height="9" fill="var(--icon)"/><path d="M40 19 L52 19 L32 74 L20 74 Z" fill="var(--icon)"/><path d="M68 19 L80 19 L100 74 L88 74 Z" fill="var(--icon)"/><rect x="36" y="48" width="50" height="8" fill="var(--icon)"/></svg>
  <span class="cat-label" style="left:656px;top:883px">TABLES</span>

  <svg class="cat-icon" style="left:958px;top:744px" width="106" height="94" viewBox="0 0 106 94"><g fill="none" stroke="var(--icon)" stroke-width="4"><path d="M53 2 L100 42 L100 88 L6 88 L6 42 Z"/><path d="M6 42 Q53 20 100 42"/><path d="M53 22 L53 88"/><path d="M30 34 L18 88 M76 34 L88 88"/></g></svg>
  <span class="cat-label" style="left:891px;top:883px">TENTS</span>

  <svg class="cat-icon" style="left:131px;top:1006px" width="120" height="120" viewBox="0 0 120 120"><path d="M92 2 L108 2 L96 56 L82 60 Z" fill="#999"/><path d="M96 56 Q100 74 80 92 L66 120 L12 120 Q40 94 60 80 Q74 66 82 60 Z" fill="var(--icon)"/></svg>
  <span class="cat-label" style="left:81px;top:1165px">BANNER BARS</span>

  <svg class="cat-icon" style="left:457px;top:1022px" width="104" height="92" viewBox="0 0 104 92"><g fill="none" stroke="var(--icon)" stroke-width="4"><path d="M52 2 L98 36 L98 90 L6 90 L6 36 Z"/><path d="M6 36 Q52 18 98 36"/><path d="M52 20 L52 90"/><path d="M28 30 L18 90 M76 30 L86 90"/></g></svg>
  <span class="cat-label" style="left:393px;top:1165px">WALLS</span>

  <svg class="cat-icon" style="left:746px;top:1032px" width="60" height="96" viewBox="0 0 60 96"><path d="M4 2 L54 2 L40 58 L20 58 Z" fill="#dcdcdc"/><path d="M16 2 L26 2 L30 50 L24 50 Z" fill="#bbb"/><circle cx="30" cy="70" r="24" fill="#bdbdbd"/><circle cx="30" cy="70" r="8" fill="#fff"/></svg>
  <span class="cat-label" style="left:656px;top:1165px">WEIGHTS</span>

  <svg class="cat-icon" style="left:975px;top:1006px" width="60" height="120" viewBox="0 0 60 120"><rect x="26" y="0" width="3" height="30" fill="#777"/><path d="M10 36 Q30 16 52 24 Q56 60 50 110 L10 110 Q6 70 10 36 Z" fill="#bdbdbd"/><rect x="8" y="100" width="46" height="6" fill="#888"/></svg>
  <span class="cat-label" style="left:885px;top:1165px">SANDBAGS</span>
</section>

<section>
  <h2 class="abs section-title" style="top:1267px">Best Selling Products</h2>

  <div class="product-img gazebo-photo" style="left:0;width:176px" role="img" aria-label="Green pop-up gazebo with side walls on a grass field"></div>
  <div class="product-img gazebo-photo" style="left:207px;width:249px" role="img" aria-label="Green pop-up gazebo with side walls on a grass field"></div>
  <div class="product-img gazebo-photo" style="left:478px;width:250px" role="img" aria-label="Green pop-up gazebo with side walls on a grass field"></div>
  <div class="product-img gazebo-photo" style="left:754px;width:249px" role="img" aria-label="Green pop-up gazebo with side walls on a grass field"></div>
  <div class="product-img gazebo-photo" style="left:1030px;width:170px" role="img" aria-label="Green pop-up gazebo with side walls on a grass field"></div>

  <svg class="chev" style="left:22px" viewBox="0 0 30 40"><path d="M22 4 L8 20 L22 36" fill="none" stroke="rgba(255,255,255,.7)" stroke-width="3"/></svg>
  <svg class="chev" style="left:1130px" viewBox="0 0 30 40"><path d="M8 4 L22 20 L8 36" fill="none" stroke="rgba(255,255,255,.7)" stroke-width="3"/></svg>

  <span class="product-name" style="left:-2px;top:1583px">Item Name</span>
  <span class="product-price" style="left:14px;top:1623px">$99.99</span>
  <span class="product-name" style="left:278px;top:1583px">Item Name</span>
  <span class="product-price" style="left:294px;top:1623px">$99.99</span>
  <span class="product-name" style="left:549px;top:1583px">Item Name</span>
  <span class="product-price" style="left:566px;top:1623px">$99.99</span>
  <span class="product-name" style="left:824px;top:1583px">Item Name</span>
  <span class="product-price" style="left:841px;top:1623px">$99.99</span>
  <span class="product-name" style="left:1101px;top:1583px">Item Name</span>
  <span class="product-price" style="left:1117px;top:1623px">$99.99</span>
</section>

<section>
  <h2 class="abs section-title" style="top:1775px">Only at Gazebrix...</h2>

  <div class="feature-img photo-bag" style="left:223px;top:1862px;width:293px;height:183px" role="img" aria-label="Black carry bag holding a folded gazebo"></div>
  <span class="feature-label" style="left:392px;top:2028px">Easy to Carry</span>

  <div class="feature-img photo-frame" style="left:661px;top:1954px;width:291px;height:189px" role="img" aria-label="Close-up of a heavy-duty metal gazebo frame joint"></div>
  <span class="feature-label" style="left:828px;top:2125px">Sturdy &amp; Tough</span>

  <div class="feature-img photo-print" style="left:226px;top:2197px;width:301px;height:177px" role="img" aria-label="Custom printed red and white gazebo on grass"></div>
  <span class="feature-label" style="left:423px;top:2358px">Customizable</span>

  <div class="feature-img photo-folded" style="left:675px;top:2262px;width:307px;height:189px" role="img" aria-label="Folded gazebo frame with red canopy standing on a lawn"></div>
  <span class="feature-label" style="left:860px;top:2445px">Easy Assemble</span>

  <div class="feature-img gazebo-photo" style="left:231px;top:2546px;width:303px;height:183px" role="img" aria-label="Green pop-up gazebo with side walls on a grass field"></div>
  <span class="feature-label" style="left:412px;top:2712px">Unbeatable Price</span>
</section>

<footer class="abs footer">
  <span class="footer-note">(Footer Info)</span>
</footer>

</body>
</html>
```